New bussiness card, using company logo.
Lachlan Voss
Manager/Director
Birch Property Developments
Po Box 4657
Glenmarra Central
Wst
0455 386 218
lachlan@birchpropertydevelopments
eye catching, vibrant colours, professional

```html
<!DOCTYPE html>
<html lang="en">
<head>
<meta charset="utf-8">
<title>Birch Property Developments – Business Card</title>
<link href="https://fonts.googleapis.com/css2?family=Arimo:wght@400;700&display=swap" rel="stylesheet">
<style>
  :root {
    --page-bg: #efe6da;
    --card-white: #ffffff;
    --card-mint: #bfe8b0;
    --brand-red: #a3331f;
    --band-red: #8e1410;
    --band-red-light: #a82418;
    --name-blue: #2a8ad8;
    --ink: #111111;
    --shadow: rgba(0,0,0,0.35);
  }
  * { box-sizing: border-box; margin: 0; padding: 0; }
  html, body { width: 1200px; height: 942px; overflow: hidden; }
  body {
    position: relative;
    background: var(--page-bg);
    font-family: "Arimo", Arial, sans-serif;
    color: var(--ink);
  }
  .card {
    position: absolute;
    overflow: hidden;
    box-shadow: 6px 8px 14px var(--shadow);
  }
  .card-back {
    left: 180px; top: 339px; width: 492px; height: 281px;
    background: var(--card-mint);
    border: 2px solid #e9f6e2;
  }
  .card-front {
    left: 602px; top: 134px; width: 498px; height: 330px;
    background: var(--card-white);
  }
  .brand-name {
    position: absolute;
    font-weight: 700;
    color: var(--brand-red);
    text-transform: uppercase;
    line-height: 1.05;
    letter-spacing: 0.5px;
  }
  .card-back .brand-name {
    left: 0; right: 0; top: 88px;
    text-align: center;
    font-size: 28px;
  }
  .card-back .email {
    position: absolute;
    left: 0; right: 0; top: 210px;
    text-align: center;
    font-size: 19px;
  }
  .card-front .brand-name {
    left: 14px; top: 118px; width: 230px;
    font-size: 24px;
  }
  .contact {
    position: absolute;
    left: 258px; top: 30px;
  }
  .contact .person {
    font-size: 25px;
    color: var(--name-blue);
  }
  .contact .role {
    font-size: 15px;
    margin-top: 2px;
  }
  .contact .details {
    margin-top: 22px;
    font-size: 10.5px;
    line-height: 1.45;
  }
  .footer-band {
    position: absolute;
    left: 0; bottom: 0;
    width: 498px; height: 100px;
    background: linear-gradient(180deg, var(--band-red-light), var(--band-red));
  }
  .label {
    position: absolute;
    font-weight: 700;
    font-size: 24px;
  }
  .label-back { left: 192px; top: 630px; }
  .label-front { left: 982px; top: 476px; }
</style>
</head>
<body>
  <section class="card card-back" aria-label="Business card back">
    <div class="brand-name">Birch Property<br>Developments</div>
    <p class="email">lachlan@birchpropertydevelopments</p>
  </section>

  <section class="card card-front" aria-label="Business card front">
    <div class="brand-name">Birch Property<br>Developments</div>
    <div class="contact">
      <p class="person">Lachlan Voss</p>
      <p class="role">Manager/Director</p>
      <p class="details">
        Birch Property Developments<br>
        Po Box 4657<br>
        Glenmarra Central<br>
        Wst<br>
        0455 386 218<br>
        lachlan@birchpropertydevelopments
      </p>
    </div>
    <div class="footer-band" role="img" aria-label="Decorative red footer band with green accent lines"></div>
  </section>

  <span class="label label-back">back</span>
  <span class="label label-front">front</span>
</body>
</html>
```